Therapy Department Recruitment Flyer

Recruitment flyer similar to nursing one attached but for Occupational Therapy and Physical Therapy. Please use pictures depicting therapy services being provided to elderly population.

```html
<!DOCTYPE html>
<html lang="en">
<head>
<meta charset="UTF-8">
<title>Therapy Positions – Silver Aspen Care Center</title>
<link rel="stylesheet" href="https://fonts.googleapis.com/css2?family=Montserrat:wght@400;500;600;700;800&display=swap">
<style>
  :root{
    --teal:#0e3b38;
    --teal-soft:#8a9e9d;
    --gray:#6e6e6e;
    --ink:#1f1f1f;
    --body:#333333;
    --page:#ffffff;
    --backdrop:#ebebeb;
  }
  *{margin:0;padding:0;box-sizing:border-box;}
  html,body{width:1200px;height:2400px;overflow:hidden;background:var(--backdrop);}
  body{font-family:"Montserrat",sans-serif;color:var(--ink);position:relative;}

  .flyer{
    position:absolute;left:40px;top:408px;width:1120px;height:1584px;overflow:hidden;
    background:linear-gradient(180deg,#dde1e3 0%,#f3f4f5 30%,#ffffff 55%);
    box-shadow:0 12px 40px rgba(0,0,0,.18);
  }
  .flyer *{position:absolute;}

  .photo-hero{
    left:0;top:0;width:640px;height:940px;
    clip-path:polygon(0 0,100% 0,100% 100%,0 83.2%);
    background:linear-gradient(90deg,#b9bec1 0%,#cfd2d4 55%,rgba(255,255,255,0) 100%);
  }
  .photo-session{
    left:500px;top:1060px;width:620px;height:470px;
    background:linear-gradient(90deg,rgba(255,255,255,0) 0%,#e2e6ea 30%,#9bb3d6 60%,#d8dade 100%);
  }
  .bands{left:0;top:0;width:1120px;height:1584px;}

  .photo-circle{border-radius:50%;border:10px solid var(--teal-soft);}
  .photo-exercise{
    left:512px;top:834px;width:264px;height:264px;
    background:radial-gradient(circle at 40% 45%,#5fc3b5 0%,#e9e2c6 50%,#e2c63e 100%);
  }
  .photo-sign{
    left:764px;top:744px;width:300px;height:300px;
    background:linear-gradient(180deg,#b9c4cc 0%,#3a3d40 35%,#4a4c4e 65%,#a49a8e 100%);
  }

  .brand{left:540px;top:92px;width:305px;text-align:center;color:var(--teal);font-weight:600;}
  .brand-dot{position:relative;display:block;width:78px;height:78px;border-radius:50%;background:var(--teal);margin:0 auto 20px;}
  .brand-name{position:relative;display:block;font-size:23px;line-height:1.25;}
  .brand-place{position:relative;display:block;font-size:20px;line-height:1.3;}

  .title{left:586px;line-height:1;font-weight:800;white-space:nowrap;}
  .title-main{font-size:84px;color:var(--teal);letter-spacing:-.5px;}
  .title-line1{top:294px;}
  .title-line2{top:370px;}
  .title-sub{color:var(--ink);font-weight:800;}
  .title-line3{top:460px;font-size:50px;}
  .title-line4{top:511px;font-size:64px;}
  .rule{height:4px;background:var(--teal);}
  .rule-title{left:588px;top:594px;width:83px;}

  .roles{left:586px;top:626px;list-style:none;}
  .role{position:relative;display:flex;align-items:center;font-size:29px;font-weight:600;color:var(--ink);height:50px;line-height:1;}
  .role svg{position:relative;width:28px;height:28px;margin-right:16px;}

  .seeking{left:60px;top:911px;width:460px;font-size:34px;line-height:41.5px;font-weight:700;color:var(--ink);}
  .seeking .accent{position:static;color:var(--teal);}
  .rule-seeking{left:60px;top:1134px;width:90px;}
  .about{left:60px;top:1160px;width:461px;font-size:18.5px;line-height:25px;color:var(--body);text-align:justify;text-align-last:left;}

  .contact-label{left:60px;top:1328px;font-size:19px;line-height:1;color:var(--body);}
  .contact-name{left:60px;top:1361px;font-size:36px;line-height:1;font-weight:700;color:var(--teal);}
  .contact-role{left:60px;top:1398px;font-size:18px;line-height:1;font-weight:500;color:var(--ink);}

  .footer-phone{left:74px;top:1476px;display:flex;align-items:center;color:#fff;font-size:34px;line-height:1;font-weight:700;}
  .footer-email{left:74px;top:1523px;display:flex;align-items:center;color:#fff;font-size:20px;line-height:1;font-weight:600;letter-spacing:.4px;}
  .footer-phone svg,.footer-email svg{position:relative;margin-right:14px;}
  .footer-phone span,.footer-email span{position:relative;}
</style>
</head>
<body>
<main class="flyer">
  <div class="photo-hero" role="img" aria-label="Photo: therapist helping an elderly woman walk with a walker"></div>
  <div class="photo-session" role="img" aria-label="Photo: physical therapist treating a patient's shoulder on a treatment table"></div>

  <svg class="bands" viewBox="0 0 1120 1584" aria-hidden="true">
    <polygon points="0,782 262,864 0,844" fill="var(--gray)"/>
    <polygon points="128,808 600,912 600,958 262,864" fill="var(--teal)"/>
    <line x1="700" y1="948" x2="820" y2="910" stroke="var(--teal)" stroke-width="5"/>
    <line x1="980" y1="768" x2="1120" y2="726" stroke="var(--teal)" stroke-width="5"/>
    <polygon points="990,786 1120,746 1120,800" fill="var(--gray)"/>
    <polygon points="0,1447 512,1447 640,1572 1120,1572 1120,1584 0,1584" fill="var(--teal)"/>
    <polygon points="548,1447 588,1447 708,1560 668,1560" fill="var(--gray)"/>
  </svg>

  <div class="photo-circle photo-exercise" role="img" aria-label="Photo: therapist guiding an elderly woman through an arm exercise"></div>
  <div class="photo-circle photo-sign" role="img" aria-label="Photo: care center entrance sign"></div>

  <div class="brand">
    <span class="brand-dot"></span>
    <span class="brand-name">Silver Aspen Care Center</span>
    <span class="brand-place">Larkton, Nevada</span>
  </div>

  <h1 class="title title-main title-line1">THERAPHY</h1>
  <div class="title title-main title-line2">POSITIONS</div>
  <div class="title title-sub title-line3">SILVER ASPEN</div>
  <div class="title title-sub title-line4">CARE CENTER</div>
  <div class="rule rule-title"></div>

  <ul class="roles">
    <li class="role">
      <svg viewBox="0 0 24 24" fill="none" stroke="var(--teal)" stroke-width="2" stroke-linecap="round"><circle cx="12" cy="4.5" r="2.5"/><path d="M12 8v7M7 11h10M12 15l-4 7M12 15l4 7"/></svg>
      Physical Therapist
    </li>
    <li class="role">
      <svg viewBox="0 0 24 24" fill="none" stroke="var(--teal)" stroke-width="2" stroke-linecap="round"><circle cx="12" cy="4.5" r="2.5"/><path d="M5 11h14M12 8v6M6 17h12M9 14h6v3M8 21h8"/></svg>
      Occupational Therapist
    </li>
  </ul>

  <h2 class="seeking"><span class="accent">WE ARE SEEKING<br>CARING AND</span><br>COMPASSIONATE<br>THERAPIST TO JOIN<br>OUR TEAM</h2>
  <div class="rule rule-seeking"></div>

  <p class="about">Silver Aspen Care Center is a Skilled Nursing Facility in Larkton, Nevada. At the heart of Aspen Valley County, Larkton is a friendly, rural mountain town in Eastern Nevada that is rich with art and history, as well as an abundance of opportunities for outdoor adventure.</p>

  <div class="contact-label">Recruiting Contact</div>
  <div class="contact-name">DANA MORROW</div>
  <div class="contact-role">Director of Rehabs</div>

  <div class="footer-phone">
    <svg width="26" height="26" viewBox="0 0 24 24" fill="none" stroke="#fff" stroke-width="2" stroke-linejoin="round"><path d="M5 3h4l2 5-2.5 1.5a11 11 0 0 0 6 6L16 13l5 2v4a2 2 0 0 1-2 2A16 16 0 0 1 3 5a2 2 0 0 1 2-2z"/></svg>
    <span>775-555-0142 EXT. 2210</span>
  </div>
  <div class="footer-email">
    <svg width="26" height="18" viewBox="0 0 26 18" fill="none" stroke="#fff" stroke-width="2"><rect x="1" y="1" width="24" height="16"/><path d="M1 1l12 9 12-9"/></svg>
    <span>dmorrow@silveraspencare.com</span>
  </div>
</main>
</body>
</html>
```